Dane Moro films- wedding and event films company website. DESKTOP AND MOBILE

We need a website for a high-end wedding and event film production company. Looking for a very modern and elegant design. my old website is www.danemorofilms.example

I like the "white/black/rose gold" color scheme of my logo.

really looking for a sleek modern design the breaths professional and artistic.

Target Market(s)

wedding and event films.

Industry/Entity Type

Film Production

Number of Pages Required

5+ page

Colors

Designer to choose colors to be used in the design.

Requirements
Must have
• website name will be www.danemorofilms.example
• tagline is "CINEMATIC STORIES ABOUT YOU"
• sections: HOME, CONTACT, ABOUT, FILMS, BLOG
• You can see my old website at danemorofilms.example
• Website about section:
• Dane Moro Films was Established with the basis of truly cinematic and artistic films in mind. Dane and his team routinely travel the globe documenting weddings and events for high profile clients and discerning couples. Dane was born and raised in Maui Hawaii and has a unique approach to his films that embody the essence of a Hollywood film. Dane has spent the last 10 years traveling the world documenting corporate events and weddings with multiple Award winning production companies. In 2017 Dane decided to establish his own brand “Dane Moro films” that will take everything he has learned with his past experiences and push it to the next level. Aside from his personal achievements, Dane is extremely passionate about his craft and always looks forward to handcrafting beautiful wedding/event films for his clients. The style of work is non-traditional and the day of filming is extremely unobtrusive (as we are looking for natural-candid/ raw emotions).
• If you are looking for the best price in town, we are probably not the best option, but if you’re looking for the best quality and peace of mind on your wedding day, then you’re in the right place. Dane Moro Films is a boutique studio that only accepts a limited number of assignments per year. Inquire early to ensure availability.
• LINKS TO VIMEO VIDEOS THAT WILL BE IN THE "FILMS' SECTION.
• BRENT FILM TRAILER - https://clipvault.example/418205736
• BRENT FEATURE FILM - https://clipvault.example/527910384
• NORA AND PAUL'S WEDDING - https://clipvault.example/649382015
• DRONE DEMO REEL - https://clipvault.example/751046923
• WEDDING INDUSTRY EVENT PARTY - https://clipvault.example/862937104/7a2d9c3e8b
• images that you can use on site are here: https://maribelortegaphotos.picvault.example/gallery/ruth&glen/
• password is: meadow

```html
<!DOCTYPE html>
<html lang="en">
<head>
<meta charset="utf-8">
<title>Dane Moro Films</title>
<link href="https://fonts.googleapis.com/css2?family=Open+Sans:wght@400;600;700&family=Oswald:wght@400;500&display=swap" rel="stylesheet">
<style>
:root{
  --rose:#e5925b;
  --rose-light:#f2ac78;
  --ink:#333333;
  --muted:#8a8a8a;
  --line:#e6e6e6;
  --paper:#ffffff;
  --grey-band:#efefef;
  --footer:#2b2b2b;
  --footer-deep:#1f1f1f;
  --social:#4a7fc1;
}
*{margin:0;padding:0;box-sizing:border-box}
html,body{width:1200px;height:3468px;overflow:hidden}
body{position:relative;background:var(--paper);font-family:"Open Sans",Arial,sans-serif;color:var(--ink)}
.abs{position:absolute}
.header-phone{left:96px;top:44px;font-size:22px;color:var(--ink);display:flex;align-items:center;gap:10px}
.brand{left:520px;top:28px;width:160px;display:flex;align-items:center;gap:10px}
.brand-mark{width:22px;height:22px;background:var(--rose);flex:none}
.brand-name{font-size:18px;font-weight:600;color:var(--ink);letter-spacing:2px;text-transform:uppercase;line-height:1.1;text-align:left}
.social-top{right:96px;top:42px;display:flex;gap:8px}
.social-top span{width:26px;height:26px;background:var(--social);display:block}
.nav{left:0;top:120px;width:1200px;height:72px;border-top:1px solid var(--line);display:flex;justify-content:center;align-items:center;gap:60px;font-size:18px;color:var(--ink);letter-spacing:1px}
.nav a{color:inherit;text-decoration:none}
.nav .current{color:var(--rose)}
.hero{left:0;top:192px;width:1200px;height:524px;background:linear-gradient(180deg,#b9c6cf 0%,#dad9d2 35%,#8c8678 62%,#4f4b44 100%)}
.hero-title{right:110px;top:500px;font-family:"Oswald",sans-serif;font-size:52px;line-height:58px;color:#fff;text-align:right;letter-spacing:1px;text-transform:uppercase}
.portrait{left:140px;top:806px;width:284px;height:284px;border-radius:50%;border:8px solid #e8e8e8;background:linear-gradient(160deg,#6d6d6d,#bdbdbd 55%,#e4e4e4)}
.about-title{left:468px;top:818px;font-family:"Oswald",sans-serif;font-size:34px;color:var(--ink);letter-spacing:1px}
.about-text{left:468px;top:872px;width:600px;font-size:15px;line-height:25px;color:var(--muted)}
.btn{display:inline-block;background:var(--rose);color:#fff;font-size:12px;letter-spacing:1px;border-radius:20px;padding:8px 22px;text-transform:uppercase}
.about-btn{left:468px;top:1060px}
.services{left:0;top:1212px;width:1200px;height:428px;background:linear-gradient(135deg,var(--rose) 0%,var(--rose-light) 50%,var(--rose) 100%)}
.section-title{left:0;width:1200px;text-align:center;font-family:"Oswald",sans-serif;font-size:36px;letter-spacing:1px;text-transform:uppercase}
.services .section-title{top:80px;color:#fff}
.service{top:170px;width:200px;text-align:center;color:#fff;font-size:16px;letter-spacing:1px;text-transform:uppercase}
.service svg{display:block;margin:0 auto 26px}
.films .section-title{top:1740px}
.thumb{width:310px;height:190px;background:linear-gradient(160deg,#8d7a68,#c9b59c 55%,#5e5144)}
.thumb .play{position:absolute;left:135px;top:75px}
.thumb-cap{width:310px;text-align:center;font-size:14px;color:var(--ink);letter-spacing:1px}
.films-btn{left:490px;top:2368px;width:220px;text-align:center;border:1px solid var(--rose);color:var(--rose);border-radius:20px;font-size:12px;padding:8px 0;letter-spacing:1px}
.blog-band{left:0;top:2500px;width:1200px;height:600px;background:var(--grey-band)}
.blog .section-title{top:2584px}
.card{top:2672px;width:310px;height:310px;background:#fff}
.card-img{width:310px;height:168px;background:linear-gradient(160deg,#4a2d3a,#b3637a 50%,#2c1c28)}
.card h3{margin-top:20px;text-align:center;font-size:16px;font-weight:600;letter-spacing:1px;color:var(--ink)}
.card p{margin:8px 30px 0;text-align:center;font-size:12px;line-height:18px;color:var(--muted)}
.card .more{display:block;text-align:center;font-size:12px;color:var(--ink);margin-top:6px}
.footer{left:0;top:3100px;width:1200px;height:320px;background:var(--footer);color:#cfcfcf}
.copy{left:0;top:3420px;width:1200px;height:48px;background:var(--footer-deep);color:#9a9a9a;font-size:12px;text-align:center;line-height:48px}
.f-brand{left:90px;top:140px;display:flex;align-items:center;gap:10px}
.f-brand .brand-name{color:#fff}
.f-col{top:58px;font-size:13px;line-height:22px}
.f-col h4{font-size:15px;font-weight:600;color:#fff;letter-spacing:1px;text-transform:uppercase;margin-bottom:12px}
.f-input{width:220px;height:30px;background:#fff;margin-top:10px;font-size:12px;color:#999;padding:0 10px;line-height:30px}
.f-submit{margin-top:10px;font-size:11px;padding:6px 16px}
.follow li{list-style:none;display:flex;align-items:center;gap:12px;margin-bottom:14px}
.follow li span{width:30px;height:30px;border-radius:50%;border:1px solid #777;display:block}
</style>
</head>
<body>

<header>
  <div class="abs header-phone">
    <svg width="18" height="18" viewBox="0 0 24 24"><path d="M6.6 10.8a15 15 0 0 0 6.6 6.6l2.2-2.2c.3-.3.7-.4 1-.2 1.1.4 2.3.6 3.6.6.6 0 1 .4 1 1V20c0 .6-.4 1-1 1C10.6 21 3 13.4 3 4c0-.6.4-1 1-1h3.5c.6 0 1 .4 1 1 0 1.3.2 2.5.6 3.6.1.3 0 .7-.2 1z" fill="#e5925b"/></svg>
    <span>808-555-0142</span>
  </div>
  <div class="abs brand"><span class="brand-mark"></span><span class="brand-name">Dane Moro<br>Films</span></div>
  <div class="abs social-top"><span></span><span></span><span></span><span></span></div>
  <nav class="abs nav">
    <a class="current">HOME</a><a>ABOUT</a><a>FILMS</a><a>BLOG</a><a>CONTACT US</a>
  </nav>
</header>

<section>
  <div class="abs hero" role="img" aria-label="Wedding couple embracing on a rocky seaside with a lighthouse behind"></div>
  <h1 class="abs hero-title">Cinematic Stories<br>About You</h1>
</section>

<section class="about">
  <div class="abs portrait" role="img" aria-label="Portrait of the filmmaker"></div>
  <h2 class="abs about-title">DANE MORO FILMS</h2>
  <p class="abs about-text">At Dane Moro Films we specialize in offering the finest in wedding and corporate videography. We offer a very modern and creative style for capturing your special moments with a beautiful and cinematic approach that enables us to produce the highest quality of films. Dane and his talented team have over 10 years of experience, and they strive to make the best films in the industry. We pride ourselves on remaining attentive to clients' needs, business practices rooted in integrity, and continually striving to be at the forefront of innovation in our industry.</p>
  <span class="abs btn about-btn">Read More</span>
</section>

<section class="abs services">
  <h2 class="abs section-title">Our Services</h2>
  <div class="abs service" style="left:100px">
    <svg width="80" height="80" viewBox="0 0 80 80"><circle cx="40" cy="40" r="38" fill="none" stroke="#fff" stroke-width="2"/><rect x="24" y="30" width="22" height="20" rx="2" fill="#fff"/><path d="M48 36l10-6v20l-10-6z" fill="#fff"/></svg>
    Corporate</div>
  <div class="abs service" style="left:370px">
    <svg width="80" height="80" viewBox="0 0 80 80"><circle cx="40" cy="40" r="38" fill="none" stroke="#fff" stroke-width="2"/><rect x="25" y="27" width="30" height="28" rx="2" fill="none" stroke="#fff" stroke-width="2"/><line x1="25" y1="35" x2="55" y2="35" stroke="#fff" stroke-width="2"/><line x1="32" y1="23" x2="32" y2="30" stroke="#fff" stroke-width="2"/><line x1="48" y1="23" x2="48" y2="30" stroke="#fff" stroke-width="2"/></svg>
    Events</div>
  <div class="abs service" style="left:630px">
    <svg width="80" height="80" viewBox="0 0 80 80"><circle cx="40" cy="40" r="38" fill="none" stroke="#fff" stroke-width="2"/><circle cx="34" cy="42" r="9" fill="none" stroke="#fff" stroke-width="2.5"/><circle cx="46" cy="42" r="9" fill="none" stroke="#fff" stroke-width="2.5"/></svg>
    Wedding</div>
  <div class="abs service" style="left:900px">
    <svg width="80" height="80" viewBox="0 0 80 80"><circle cx="40" cy="40" r="38" fill="none" stroke="#fff" stroke-width="2"/><rect x="24" y="29" width="32" height="22" rx="5" fill="#fff"/><path d="M36 34l9 6-9 6z" fill="#e5925b"/></svg>
    Film</div>
</section>

<section class="films">
  <h2 class="abs section-title">Films</h2>
  <div class="abs thumb" style="left:110px;top:1840px" role="img" aria-label="Still from a wedding film"><svg class="play" width="40" height="40" viewBox="0 0 40 40"><circle cx="20" cy="20" r="19" fill="rgba(0,0,0,.45)" stroke="#fff"/><path d="M16 13l11 7-11 7z" fill="#fff"/></svg></div>
  <div class="abs thumb" style="left:445px;top:1840px" role="img" aria-label="Still from a film trailer"><svg class="play" width="40" height="40" viewBox="0 0 40 40"><circle cx="20" cy="20" r="19" fill="rgba(0,0,0,.45)" stroke="#fff"/><path d="M16 13l11 7-11 7z" fill="#fff"/></svg></div>
  <div class="abs thumb" style="left:780px;top:1840px;background:linear-gradient(180deg,#7ea6cf,#c8d5dc 40%,#3d6e5a)" role="img" aria-label="Aerial mountain lake landscape"><svg class="play" width="40" height="40" viewBox="0 0 40 40"><circle cx="20" cy="20" r="19" fill="rgba(0,0,0,.45)" stroke="#fff"/><path d="M16 13l11 7-11 7z" fill="#fff"/></svg></div>
  <div class="abs thumb-cap" style="left:110px;top:2050px">NORA AND PAUL'S WEDDING</div>
  <div class="abs thumb-cap" style="left:445px;top:2050px">BRENT FILM TRAILER</div>
  <div class="abs thumb-cap" style="left:780px;top:2050px">DRONE DEMO REEL</div>

  <div class="abs thumb" style="left:110px;top:2090px" role="img" aria-label="Couple outdoors on their wedding day"><svg class="play" width="40" height="40" viewBox="0 0 40 40"><circle cx="20" cy="20" r="19" fill="rgba(0,0,0,.45)" stroke="#fff"/><path d="M16 13l11 7-11 7z" fill="#fff"/></svg></div>
  <div class="abs thumb" style="left:445px;top:2090px;background:linear-gradient(180deg,#9fbbd6,#e3e3dc 45%,#4e6f3f)" role="img" aria-label="Grand white estate on a green lawn"><svg class="play" width="40" height="40" viewBox="0 0 40 40"><circle cx="20" cy="20" r="19" fill="rgba(0,0,0,.45)" stroke="#fff"/><path d="M16 13l11 7-11 7z" fill="#fff"/></svg></div>
  <div class="abs thumb" style="left:780px;top:2090px;background:linear-gradient(160deg,#3a2f2a,#8a6f5b 50%,#2a221e)" role="img" aria-label="Guests at an evening event party"><svg class="play" width="40" height="40" viewBox="0 0 40 40"><circle cx="20" cy="20" r="19" fill="rgba(0,0,0,.45)" stroke="#fff"/><path d="M16 13l11 7-11 7z" fill="#fff"/></svg></div>
  <div class="abs thumb-cap" style="left:110px;top:2298px">BRENT FEATURE FILM</div>
  <div class="abs thumb-cap" style="left:445px;top:2298px">DOLOREM IPSUM QUIA</div>
  <div class="abs thumb-cap" style="left:780px;top:2298px">WEDDING INDUSTRY EVENT PARTY</div>
  <div class="abs films-btn">SEE MORE OF OUR WORK</div>
</section>

<section class="blog">
  <div class="abs blog-band"></div>
  <h2 class="abs section-title">Latest Blog</h2>
  <article class="abs card" style="left:110px">
    <div class="card-img" role="img" aria-label="Reception dance floor at night"></div>
    <h3>NEQUE PORRO QUISQUAM</h3>
    <p>A fine moment we recently captured with a lovely couple, full of light and laughter on their big day.</p>
    <span class="more">Read More »</span>
  </article>
  <article class="abs card" style="left:445px">
    <div class="card-img" style="background:linear-gradient(160deg,#2d3a4a,#7a8fa6 50%,#3a2a30)" role="img" aria-label="Wedding guests in a decorated hall"></div>
    <h3>NEQUE PORRO QUISQUAM</h3>
    <p>A fine moment we recently captured with a lovely couple, full of light and laughter on their big day.</p>
    <span class="more">Read More »</span>
  </article>
  <article class="abs card" style="left:780px">
    <div class="card-img" style="background:linear-gradient(160deg,#3a1e3e,#a0487a 50%,#241426)" role="img" aria-label="Party guests under purple lights"></div>
    <h3>NEQUE PORRO QUISQUAM</h3>
    <p>A fine moment we recently captured with a lovely couple, full of light and laughter on their big day.</p>
    <span class="more">Read More »</span>
  </article>
</section>

<footer class="abs footer">
  <div class="abs f-brand"><span class="brand-mark"></span><span class="brand-name">Dane Moro<br>Films</span></div>
  <div class="abs f-col" style="left:380px;width:250px">
    <h4>Newsletter Sign Up</h4>
    <p>Sign up for our daily email by entering your information below</p>
    <div class="f-input">Email Address</div>
    <span class="btn f-submit">Subscribe</span>
  </div>
  <div class="abs f-col" style="left:700px;width:230px">
    <h4>Get In Touch</h4>
    <p>Address: 120 Harbor Lane,<br>Suite 4 Kahului</p>
    <p>Phone: <span style="color:#fff;font-size:16px">808-555-0142</span></p>
    <p>Email: info@danemorofilms.example</p>
  </div>
  <div class="abs f-col follow" style="left:980px;width:160px">
    <h4>Follow Us On</h4>
    <ul>
      <li><span></span>Social Page</li>
      <li><span></span>News Feed</li>
      <li><span></span>Photo Feed</li>
    </ul>
  </div>
</footer>
<div class="abs copy">Copyright © 2017. All Rights Reserved</div>

</body>
</html>
```